Redesign of key pages of website

We have a website in development: (You can see the test version here: https://staging.pawvira.ai) We want a redesign of a) the home page, b) the set up screens (all four steps), c) the account home page, and the chat page (all four linked below). It needs to look amazing in both desktop and mobile. Also, the chat page needs to have a few different versions to give people a choice between them.

Four areas:
1) Home page: https://staging.pawvira.ai/
2) Account pages: https://staging.pawvira.ai/account/chatsettings.php?step=1
3) Account home page (you'll need to set up an account which is free): https://staging.pawvira.ai/account/summary.php
4) Chat page: https://staging.pawvira.ai/chat.php?id=375

Also to clarify re: code, I don't need any of the interaction/behavior code. I just need the basic HTML and stylesheets so I can integrate that into the existing website.

Please feel free to pass by early versions to me or if you have any clarifications, let me know!

Industry/Entity Type

small businesses

Coding

Coded - Design and coding required

Number of Pages Required

5+ page

Font styles to use
Other font styles liked:
• keep the current font.

Requirements
Must have
• All the same elements/functionality on the current site. Just want a redesign. Also keep the dog visual. Also must work great in mobile and desktop and be really fun and modern and easy.
Nice to have
• Also in the setup pages, need a much better form of navigation (currently just have four circles.)

```html
<!DOCTYPE html>
<html lang="en">
<head>
<meta charset="utf-8">
<title>Pawvira – Private Beta</title>
<link href="https://fonts.googleapis.com/css2?family=League+Spartan:wght@700;800&family=Nunito:wght@800;900&family=Roboto:wght@400;500;700&display=swap" rel="stylesheet">
<style>
:root{
  --blue:#1f6ff5;
  --blue-deep:#0f5ce8;
  --blue-dot:#2b6cf2;
  --ink:#1b1b1f;
  --body:#4a4d55;
  --hero-bg:#e6eefc;
  --lavender:#e9ecfd;
  --navy-text:#0c1f8c;
  --green-bg:#f1faf1;
  --green-line:#78b77e;
  --green-blob:#d6ecd6;
  --pink:#f8bec3;
  --pink-soft:#fdeeee;
  --pink-blob:#fde4e4;
  --footer:#2c3f8e;
  --white:#fff;
  --orange:#f08a4b;
}
*{box-sizing:border-box;margin:0;padding:0}
html,body{width:1200px;height:2531px;overflow:hidden}
body{position:relative;background:var(--white);font-family:"Roboto",sans-serif;color:var(--body)}
.abs{position:absolute}
.heading{font-family:"League Spartan",sans-serif;font-weight:800;color:var(--ink);letter-spacing:.5px;text-transform:uppercase;line-height:1.15}
.wordmark{font-family:"Nunito",sans-serif;font-weight:900;color:var(--blue)}
.btn{position:absolute;display:flex;align-items:center;justify-content:center;background:var(--blue);color:var(--white);font-size:12px;font-weight:500;border-radius:2px}
.lead{font-size:11.5px;line-height:19px;color:var(--body)}

/* hero */
.hero{position:absolute;left:0;top:0;width:1200px;height:566px;background:linear-gradient(180deg,#eaf0fd 0%,#e1eafb 100%);overflow:hidden}
.hero-ghost{position:absolute;left:0;top:330px;font-family:"League Spartan",sans-serif;font-weight:800;font-size:300px;color:#d9e4fa;line-height:1;letter-spacing:-4px;white-space:nowrap}
.nav{position:absolute;top:43px;left:468px;display:flex;gap:22px;font-size:11px;font-weight:500;color:var(--ink)}
.nav .active{color:var(--blue)}
.beta{position:absolute;left:112px;top:74px;font-size:10.5px;color:#e53935}
.chat-frame{position:absolute;left:605px;top:178px;width:290px;height:238px;background:var(--blue);border-radius:20px}
.chat-inner{position:absolute;left:24px;top:25px;width:258px;height:200px;background:var(--white);border-radius:4px;padding:30px 0 0 37px;font-size:12px;line-height:19px;color:var(--ink)}
.mascot{position:absolute;border-radius:46% 50% 44% 48%/48% 44% 54% 50%;background:radial-gradient(circle at 40% 40%,#c7cffd 0%,#8fa3f7 55%,#3d7af0 100%)}

/* timeline */
.dot{position:absolute;width:26px;height:26px;border-radius:50%;display:flex;align-items:center;justify-content:center}
.dot i{width:9px;height:9px;border-radius:50%;display:block}
.vline{position:absolute;left:597px;width:1px}

/* share mockup */
.card{position:absolute;background:var(--white);border-radius:4px;box-shadow:0 4px 18px rgba(40,60,140,.12)}
.social-row{position:absolute;left:98px;top:118px;display:flex;gap:20px}
.social-row i{width:18px;height:18px;border-radius:50%;background:var(--blue-deep);display:block}
.msg{font-size:11px;line-height:18px;color:var(--ink)}

/* calendar */
.green{position:absolute;left:0;top:1066px;width:1200px;height:387px;background:var(--green-bg)}
.time{position:absolute;left:637px;width:148px;height:48px;background:var(--white);border:1px solid #cfd8cf;border-radius:4px;display:flex;align-items:center;justify-content:center;font-weight:700;font-size:14px;color:var(--ink)}
.cal{position:absolute;left:765px;top:1128px;width:318px;height:265px;background:var(--white);border:1px solid #dfe3ea;border-radius:4px}
.wd{position:absolute;top:103px;width:40px;margin-left:-20px;text-align:center;font-size:9px;color:#333}
.day{position:absolute;width:34px;height:34px;margin:-17px 0 0 -17px;border-radius:50%;display:flex;align-items:center;justify-content:center;font-size:11px;font-weight:700;color:var(--blue-deep);background:#e9effd}
.day.off{background:none;color:#777;font-weight:400}
.day.sel{background:var(--blue-deep);color:var(--white)}
.arrow{position:absolute;width:30px;height:30px;margin:-15px 0 0 -15px;border-radius:50%;background:#e9effd;display:flex;align-items:center;justify-content:center}

/* leads table */
.table{position:absolute;left:113px;top:1545px;width:444px;height:352px;background:var(--pink);border-radius:4px;box-shadow:0 6px 18px rgba(240,130,140,.25)}
.th{position:absolute;top:0;height:55px;display:flex;align-items:center;justify-content:center;color:var(--white);font-weight:700;font-size:14px}
.tbody{position:absolute;left:12px;top:55px;width:420px;height:286px;background:var(--white)}
.item{position:absolute;left:20px;width:230px;padding-left:30px;font-size:10px;line-height:18px;color:var(--ink)}
.item::before{content:"";position:absolute;left:13px;top:6px;width:6px;height:6px;border-radius:50%;background:#f4a7ad}
.item.band{background:var(--pink-soft);padding-top:7px;padding-bottom:7px}
.item.band::before{top:13px}
.email{position:absolute;left:288px;font-size:10px;color:var(--ink)}

/* cta */
.cta{position:absolute;left:113px;top:1998px;width:842px;height:228px;background:var(--blue);border-radius:10px}
.cta .heading{position:absolute;left:0;top:67px;width:100%;text-align:center;color:var(--white);font-size:36px}
.cta-btn{position:absolute;left:345px;top:132px;width:153px;height:40px;background:var(--white);color:var(--blue);font-size:11.5px;font-weight:500;border-radius:2px;display:flex;align-items:center;justify-content:center}

/* footer */
.footer{position:absolute;left:0;top:2302px;width:1200px;height:229px;background:var(--footer);color:var(--white)}
.ft-title{position:absolute;top:38px;font-size:18px;font-weight:500}
.ft-links{position:absolute;top:78px;font-size:11px;line-height:22.5px}
.ft-social{position:absolute;left:608px;top:78px;font-size:11px}
.ft-social div{display:flex;align-items:center;gap:14px;height:31.5px}
.ft-social i{width:17px;height:17px;border-radius:50%;border:2px solid var(--white);display:block}
</style>
</head>
<body>

<!-- hero -->
<section class="hero">
  <div class="hero-ghost" aria-hidden="true">Pawvira</div>
  <div class="abs wordmark" style="left:112px;top:26px;font-size:32px;color:#35363c">Pawvira</div>
  <div class="beta">private beta</div>
  <nav class="nav"><span class="active">Home</span><span>Account</span><span>Chat</span><span>Blog</span><span>Contact Us</span></nav>
  <div class="btn" style="left:963px;top:33px;width:124px;height:34px;font-size:11px">Login or Register</div>

  <h1 class="heading abs" style="left:112px;top:212px;font-size:34px;line-height:45px">Welcome!<br>Pawvira Private Beta</h1>
  <p class="lead abs" style="left:112px;top:322px;width:340px">Vira talks to your leads, qualifies them, and gets them on your calendar.</p>
  <div class="btn" style="left:113px;top:388px;width:124px;height:40px">See an example!</div>
  <div class="btn" style="left:260px;top:388px;width:154px;height:40px">Create your Vira now!</div>

  <div class="chat-frame">
    <div class="chat-inner">
      <div style="display:flex;align-items:center;gap:10px;margin-bottom:18px">
        <span style="width:18px;height:18px;border-radius:50%;background:var(--blue)"></span>
        <span class="wordmark" style="font-size:20px">Pawvira</span>
      </div>
      <p>Hi! I'am Vira , Maren's<br>assistant</p>
      <p style="margin-top:18px">How did you hear about<br>Maren?</p>
    </div>
  </div>
  <div class="mascot" role="img" aria-label="Blue puppy mascot illustration" style="left:832px;top:160px;width:254px;height:258px"></div>
</section>

<!-- customize and share -->
<div class="abs" style="left:280px;top:635px;width:270px;height:320px;border-radius:50% 45% 50% 40%;background:#d5e0fb"></div>
<div class="card" style="left:234px;top:679px;width:284px;height:243px">
  <div class="abs" style="left:21px;top:19px;width:241px;height:206px;background:var(--lavender);border:1px solid #d6dcf7;border-radius:4px">
    <div class="abs" style="left:24px;top:17px;width:57px;height:57px;border-radius:50%;border:2px solid var(--orange)"></div>
    <div class="abs" style="left:106px;top:30px;font-weight:700;font-size:18px;color:var(--navy-text)">Maren Hair</div>
    <div class="abs" style="left:106px;top:58px;font-size:11px;color:#555">Hairdresser/Stylist</div>
    <div class="social-row"><i></i><i></i><i></i><i></i></div>
    <div class="abs wordmark" style="left:96px;top:152px;font-size:18px">Pawvira</div>
  </div>
</div>
<div class="card" style="left:134px;top:789px;width:194px;height:165px;border:1px solid #e3e6f0">
  <p class="msg abs" style="left:0;top:0;width:100%;padding:14px 0 6px 33px;background:#f7f8fc">Hi! I'am Vira , Maren's<br>assistant</p>
  <p class="msg abs" style="left:33px;top:70px">How did you hear about<br>Maren?</p>
  <div class="abs" style="left:15px;top:123px;width:164px;height:28px;background:var(--blue);border-radius:2px;color:var(--white);font-size:7.5px;padding:10px 0 0 28px">Enter Your Message
    <svg class="abs" style="right:10px;top:7px" width="14" height="14" viewBox="0 0 14 14"><path d="M1 7 13 1 9 13 7 8Z" fill="none" stroke="#fff" stroke-width="1.4" stroke-linejoin="round"/></svg>
  </div>
</div>

<div class="dot" style="left:584px;top:766px;background:#e4ebfd"><i style="background:var(--blue-dot)"></i></div>
<div class="vline" style="top:806px;height:250px;background:var(--blue-dot)"></div>
<h2 class="heading abs" style="left:663px;top:763px;font-size:34px">Customize and Share</h2>
<p class="lead abs" style="left:663px;top:822px;width:380px">Customize the appearance, conversation, and much more. You can then share Vira by embedding it in your website or via a personalized link.</p>

<!-- qualify and schedule -->
<section class="green"></section>
<div class="dot" style="left:584px;top:1075px;background:#d9efd9"><i style="background:var(--green-line)"></i></div>
<div class="vline" style="top:1110px;height:325px;background:var(--green-line)"></div>
<h2 class="heading abs" style="left:112px;top:1216px;font-size:34px">Qualify and Schedule</h2>
<p class="lead abs" style="left:112px;top:1263px;width:380px">Get the information you need from your customers. After they meet your criteria, they can book a meeting directly on your calendar.</p>

<div class="abs" style="left:790px;top:1092px;width:322px;height:333px;border-radius:48% 52% 45% 55%;background:var(--green-blob)"></div>
<div class="cal">
  <div class="abs" style="left:30px;top:26px;font-size:14px;font-weight:500;color:var(--ink)">Select a Date &amp; Time</div>
  <div class="arrow" style="left:92px;top:65px"><svg width="10" height="10" viewBox="0 0 10 10"><path d="M6.5 1.5 3 5l3.5 3.5" fill="none" stroke="#1f6ff5" stroke-width="1.6"/></svg></div>
  <div class="abs" style="left:130px;top:58px;width:70px;text-align:center;font-size:12px;color:var(--ink)">June 2023</div>
  <div class="arrow" style="left:234px;top:65px"><svg width="10" height="10" viewBox="0 0 10 10"><path d="M3.5 1.5 7 5 3.5 8.5" fill="none" stroke="#1f6ff5" stroke-width="1.6"/></svg></div>
  <div class="wd" style="left:38px">SUN</div><div class="wd" style="left:80px">MON</div><div class="wd" style="left:121px">TUE</div><div class="wd" style="left:164px">WED</div><div class="wd" style="left:205px">THU</div><div class="wd" style="left:247px">FRI</div><div class="wd" style="left:288px">SAT</div>
  <div class="day" style="left:205px;top:138px">1</div><div class="day" style="left:247px;top:138px">2</div><div class="day off" style="left:288px;top:138px">3</div>
  <div class="day off" style="left:38px;top:178px">4</div><div class="day" style="left:80px;top:178px">5</div><div class="day" style="left:121px;top:178px">6</div><div class="day" style="left:164px;top:178px">7</div><div class="day" style="left:205px;top:178px">8</div><div class="day" style="left:247px;top:178px">9</div><div class="day off" style="left:288px;top:178px">10</div>
  <div class="day off" style="left:38px;top:219px">11</div><div class="day" style="left:80px;top:219px">12</div><div class="day sel" style="left:121px;top:219px">13</div><div class="day" style="left:164px;top:219px">14</div><div class="day" style="left:205px;top:219px">15</div><div class="day" style="left:247px;top:219px">16</div><div class="day off" style="left:288px;top:219px">17</div>
</div>
<div class="time" style="top:1176px">10:00 am</div>
<div class="time" style="top:1236px">10:00 am</div>
<div class="time" style="top:1296px">10:00 am</div>

<!-- manage leads -->
<div class="dot" style="left:584px;top:1465px;background:#fde6e6"><i style="background:#f4a7ad"></i></div>
<div class="vline" style="top:1508px;height:410px;background:#f4a7ad"></div>
<div class="dot" style="left:584px;top:1934px;background:#e4ebfd"><i style="background:var(--blue-dot)"></i></div>

<div class="abs" style="left:65px;top:1486px;width:470px;height:436px;border-radius:45% 55% 48% 52%;background:var(--pink-blob)"></div>
<div class="table">
  <div class="th" style="left:0;width:282px">Summary</div>
  <div class="th" style="left:282px;width:162px">Email</div>
  <div class="abs" style="left:282px;top:0;width:2px;height:352px;background:var(--white)"></div>
  <div class="tbody">
    <div class="abs" style="left:270px;top:0;width:1px;height:286px;background:#f3d4d6"></div>
    <div class="abs" style="left:0;top:156px;width:420px;height:1px;background:#f3d4d6"></div>
    <div class="item" style="top:12px">Interested in a fitness coach</div>
    <div class="item band" style="top:37px">Does not currently work out</div>
    <div class="item" style="top:79px">Specifically interested in arms and strength</div>
    <div class="item band" style="top:105px">In the Seattle area and flexible on time</div>
    <div class="item" style="top:169px">Interested in a new fitness coach</div>
    <div class="item band" style="top:193px">Works out 3 times a week</div>
    <div class="item" style="top:239px">Has a fitness instructor now but his approach is too relaxed</div>
    <div class="email" style="top:73px">joel.tanner@mailbox.test</div>
    <div class="email" style="top:220px">nora.linden@mailbox.test</div>
  </div>
</div>
<h2 class="heading abs" style="left:663px;top:1666px;font-size:34px">Manage Your Leads</h2>
<p class="lead abs" style="left:663px;top:1713px;width:400px">Get notified via email or text. See a summary of each lead and manage them in one place. Search, sort, add notes, and more.</p>

<!-- call to action -->
<section class="cta">
  <h2 class="heading">Let Vira handle your leads today!</h2>
  <div class="cta-btn">Create your Vira now!</div>
</section>
<div class="mascot" role="img" aria-label="Blue puppy mascot illustration" style="left:876px;top:2024px;width:230px;height:256px"></div>

<!-- footer -->
<footer class="footer">
  <div class="abs wordmark" style="left:112px;top:28px;font-size:32px;color:var(--white)">Pawvira</div>
  <div class="abs" style="left:112px;top:103px;font-size:11px">© 2023 Pawvira.ai. All rights reserved</div>
  <div class="ft-title" style="left:402px">Quick Link</div>
  <div class="ft-links" style="left:403px">Home<br>Account<br>Chat<br>Blog<br>Contact</div>
  <div class="ft-title" style="left:608px">Follow Us</div>
  <div class="ft-social">
    <div><i></i>Linkora</div><div><i></i>Chirpa</div><div><i></i>Pixelle</div><div><i></i>Reelio</div>
  </div>
  <div class="ft-title" style="left:808px">Subscribe To Our Newsletter</div>
  <div class="abs" style="left:808px;top:72px;width:274px;height:36px;border:1px solid var(--white);border-radius:2px;font-size:8.5px;padding:12px 0 0 12px">Enter your email</div>
  <div class="abs" style="left:808px;top:122px;width:274px;height:36px;background:var(--blue-deep);border-radius:2px;display:flex;align-items:center;justify-content:center;font-size:11px;font-weight:700">Subscribe Now</div>
</footer>

</body>
</html>
```